Webdesign für Metallverarbeitung
Zielgruppe
Metallverarbeitung, Verpackung, Automobilzulieferer, Lasertechnik, Elektrotechnik, CAD Verarbeitung
Aufgabenstellung
-Farbe: Blau/Silber Edelstahllook,
-Logo anbei
- Modernes Team, Flexibilität, Dynamik
- Metallverarbeitendes Unternehmen
- Automobil
-Elektroindustrie

```html
<!DOCTYPE html>
<html lang="de">
<head>
<meta charset="utf-8">
<title>Stahlform Keller – Webdesign Desktop &amp; Mobil</title>
<link href="https://fonts.googleapis.com/css2?family=Poppins:wght@400;500;600;700&display=swap" rel="stylesheet">
<style>
  :root{
    --brand-blue:#003354;
    --brand-black:#212121;
    --page-bg:#f7f8f9;
    --sidebar-bg:#f1f2f3;
    --hero-dark:#14202b;
    --hero-steel:#2f4a60;
    --hero-spark:#8a6a3e;
    --text-light:#ffffff;
    --text-muted:#dfe5ea;
  }
  *{box-sizing:border-box;margin:0;padding:0}
  html,body{width:900px;height:1200px;overflow:hidden}
  body{background:var(--page-bg);font-family:'Poppins',sans-serif;position:relative}

  /* ---------- Desktop view ---------- */
  .desktop{position:absolute;left:20px;top:40px;width:860px;height:452px;overflow:hidden;box-shadow:0 14px 30px rgba(0,0,0,.18)}
  .desktop .hero-photo{position:absolute;inset:0;
    background:
      radial-gradient(ellipse 38% 45% at 58% 62%, rgba(200,150,80,.55), transparent 70%),
      radial-gradient(ellipse 30% 40% at 80% 35%, rgba(90,110,120,.55), transparent 70%),
      linear-gradient(120deg,var(--hero-steel) 0%,#1f3446 45%,var(--hero-dark) 75%,var(--hero-spark) 100%)}
  .desktop .sidebar-stripe{position:absolute;left:0;top:0;width:160px;height:100%;background:var(--brand-blue);
    clip-path:polygon(0 0,100% 0,88% 100%,0 100%)}
  .desktop .sidebar{position:absolute;left:0;top:0;width:152px;height:100%;background:var(--sidebar-bg);
    clip-path:polygon(0 0,100% 0,88% 100%,0 100%)}
  .brand{position:absolute;left:10px;top:34px;display:flex;align-items:center;gap:6px;color:var(--brand-blue);font-weight:600;font-size:11px;line-height:1.15}
  .brand-dot{width:16px;height:16px;border-radius:50%;background:var(--brand-blue);flex:none}
  .nav{position:absolute;left:0;top:100px;width:146px;list-style:none}
  .nav li{height:26px;line-height:26px;padding-left:16px;font-size:9.5px;color:var(--brand-black)}
  .nav li::before{content:"»";margin-right:5px;font-weight:600}
  .nav li.is-active{background:var(--brand-blue);color:var(--text-light)}
  .copyright{position:absolute;left:4px;top:385px;width:128px;font-size:6.5px;line-height:1.5;color:var(--brand-black)}
  .social{position:absolute;left:6px;top:424px;display:flex;gap:9px}
  .social span{width:9px;height:9px;border-radius:50%;background:var(--brand-blue)}

  .contact{position:absolute;right:16px;top:18px;display:flex;align-items:center;gap:6px;color:var(--text-light);font-size:11px}
  .contact strong{font-weight:500;font-size:12px}
  .hero-text{position:absolute;left:178px;top:96px;width:360px;color:var(--text-light)}
  .hero-title{font-weight:700;font-size:50px;line-height:1.12;letter-spacing:-.5px}
  .hero-sub{font-size:21px;line-height:1.25;margin-top:2px}
  .hero-copy{font-size:10.5px;line-height:1.6;color:var(--text-muted);margin-top:14px;padding-left:7px;width:290px}

  /* ---------- Mobile view ---------- */
  .mobile{position:absolute;left:300px;top:540px;width:300px;height:600px;overflow:hidden;box-shadow:0 14px 30px rgba(0,0,0,.18)}
  .mobile .hero-photo{position:absolute;inset:0;
    background:
      radial-gradient(ellipse 55% 30% at 70% 62%, rgba(200,150,80,.5), transparent 70%),
      radial-gradient(ellipse 50% 25% at 55% 30%, rgba(100,115,120,.55), transparent 70%),
      linear-gradient(180deg,#ffffff 0%,#e9ecef 7%,var(--hero-steel) 20%,#1d2f3f 55%,var(--hero-dark) 80%,#5a4a33 100%)}
  .mobile-bar{position:absolute;left:10px;right:12px;top:14px;display:flex;align-items:center;justify-content:space-between}
  .mobile-bar .brand{position:static;font-size:9px}
  .mobile-bar .brand-dot{width:13px;height:13px}
  .mobile-icons{display:flex;align-items:center;gap:7px}
  .mobile-icons span{width:8px;height:8px;border-radius:50%;background:var(--brand-black)}
  .menu-lines{display:flex;flex-direction:column;gap:2px;margin-left:18px}
  .menu-lines i{display:block;height:2px;background:var(--brand-black)}
  .mobile .hero-text{left:12px;top:238px;width:280px}
  .mobile .hero-title{font-size:42px;line-height:1.15}
  .mobile .hero-sub{font-size:18px;line-height:1.25}
  .mobile .hero-copy{font-size:12.5px;line-height:1.55;padding-left:2px;width:276px;margin-top:10px}
</style>
</head>
<body>

<section class="desktop" aria-label="Startseite Desktop-Ansicht">
  <div class="hero-photo" role="img" aria-label="Foto: Laserschneidkopf einer Metallbearbeitungsmaschine mit Funkenflug auf Blech"></div>
  <div class="sidebar-stripe"></div>
  <aside class="sidebar">
    <div class="brand"><span class="brand-dot"></span><span>Stahlform<br>Keller GmbH</span></div>
    <ul class="nav">
      <li class="is-active">Über uns</li>
      <li>Dienstleistungen</li>
      <li>Verweise</li>
      <li>Galerie</li>
      <li>Kontakt</li>
      <li>AGB</li>
      <li>Impressum</li>
      <li>Datenschutz</li>
    </ul>
    <p class="copyright">Copyright © 2018 Stahlform<br>Keller GmbH.<br>Alle Rechte vorbehalten.</p>
    <div class="social" aria-label="Soziale Netzwerke"><span></span><span></span><span></span><span></span></div>
  </aside>
  <div class="contact">
    <svg width="12" height="12" viewBox="0 0 24 24" aria-hidden="true"><path fill="#fff" d="M6.6 10.8a15.2 15.2 0 0 0 6.6 6.6l2.2-2.2c.3-.3.7-.4 1-.2 1.1.4 2.3.6 3.6.6.6 0 1 .4 1 1V20c0 .6-.4 1-1 1A17 17 0 0 1 3 4c0-.6.4-1 1-1h3.5c.6 0 1 .4 1 1 0 1.3.2 2.5.6 3.6.1.3 0 .7-.2 1z"/></svg>
    <span>Einen Termin verabreden ? <strong>+49 700 5550142</strong></span>
  </div>
  <div class="hero-text">
    <h1 class="hero-title">“MADE IN GERMANY”</h1>
    <p class="hero-sub">– wir halten unser Qualitätsversprechen!</p>
    <p class="hero-copy">Wir sind Ihr zuverlässigster Partner von der Konstruktion/ Entwicklung bis zum fertig veredelten Endprodukt. Dabei denken wir innovativ, arbeiten kreativ und kombinieren die traditionelle Handwerkskunst mit aktuellem Design.</p>
  </div>
</section>

<section class="mobile" aria-label="Startseite Mobil-Ansicht">
  <div class="hero-photo" role="img" aria-label="Foto: Laserschneidkopf mit Funkenflug, hochkant"></div>
  <div class="mobile-bar">
    <div class="brand"><span class="brand-dot"></span><span>Stahlform<br>Keller GmbH</span></div>
    <div class="mobile-icons" aria-label="Soziale Netzwerke und Menü">
      <span></span><span></span><span></span><span></span>
      <div class="menu-lines"><i style="width:11px"></i><i style="width:8px"></i><i style="width:11px"></i></div>
    </div>
  </div>
  <div class="hero-text">
    <h1 class="hero-title">“MADE IN GERMANY”</h1>
    <p class="hero-sub">– wir halten unser Qualitätsversprechen!</p>
    <p class="hero-copy">Wir sind Ihr zuverlässigster Partner von der Konstruktion/ Entwicklung bis zum fertig veredelten Endprodukt. Dabei denken wir innovativ, arbeiten kreativ und kombinieren die traditionelle Handwerkskunst mit aktuellem Design.</p>
  </div>
</section>

</body>
</html>
```